Bourbon label design for bourbon brand. Looking to freshen our current label.

I need a Bourbon label design for our rebranded Bourbon bottle. Label should include picture of our horse and our logo on the bottle. Front Label is 3.5 inches wide and 6 inches tall, back label is 4 inches tall and 3 inches wide. Back label can be a simple plain logo like the one in the brief. I have included a design of our current bottle and label. We want to stay close to the current color schemes but want a fresh rebrand of the design. The label needs to be the correct size on a tall bottle like pictured.

Target Market(s)

Our Bourbon members, 30-50 year old males

Requirements
Must have
• Picture of our horse, our B logo , straight Bourbon whiskey on the front. Room to edit text on the back label.

```html
<!DOCTYPE html>
<html lang="en">
<head>
<meta charset="utf-8">
<title>Nightfall Straight Bourbon Whiskey – Label Set</title>
<link href="https://fonts.googleapis.com/css2?family=Playfair+Display:wght@800&family=Domine:wght@400;700&family=Oswald:wght@300;400&family=Pinyon+Script&display=swap" rel="stylesheet">
<style>
  :root{
    --page:#f4f3f1;
    --label-dark:#2c2c2c;
    --label-mid:#4a4a4a;
    --ink:#f2f2f2;
    --ink-soft:#cfcfcf;
    --ink-muted:#a9a9a9;
    --field:#bdbdbd;
    --rule:#9a9a9a;
    --photo-light:#9c9c9c;
    --photo-dark:#3e3e3e;
  }
  *{margin:0;padding:0;box-sizing:border-box}
  html,body{width:900px;height:1200px;overflow:hidden;background:var(--page)}
  .canvas{position:relative;width:900px;height:1200px}

  .label{position:absolute;color:var(--ink);text-align:center;overflow:hidden;
    background:linear-gradient(90deg,var(--label-dark) 0%,var(--label-mid) 50%,var(--label-dark) 100%)}
  .front-label{left:90px;top:215px;width:330px;height:770px}
  .back-label{left:480px;top:255px;width:330px;height:690px}

  .abs{position:absolute;left:0;right:0}

  /* front */
  .horse-photo{position:absolute;left:105px;top:60px;width:140px;height:240px;
    border-radius:45% 45% 30% 30%;
    background:radial-gradient(ellipse at 50% 40%,var(--photo-light) 0%,#6d6d6d 55%,var(--photo-dark) 100%)}
  .est-tag{position:absolute;top:198px;width:30px;font-family:"Oswald",sans-serif;font-weight:300;
    font-size:13px;color:var(--ink-muted);border-top:1px solid var(--rule);border-bottom:1px solid var(--rule);
    padding:5px 0;line-height:1}
  .est-tag.left{left:38px}
  .est-tag.right{right:30px}
  .brand-wordmark{top:268px;display:flex;justify-content:center;font-family:"Playfair Display",serif;font-weight:800;
    font-size:96px;line-height:1;color:var(--ink)}
  .brand-wordmark span{display:block;flex:none;transform:scaleX(.5);transform-origin:center;letter-spacing:1px;white-space:nowrap}
  .product-line{top:386px}
  .product-type{display:inline-block;font-family:"Domine",serif;font-size:19px;color:var(--ink-soft);letter-spacing:.3px;
    transform:scaleX(.85);white-space:nowrap}
  .side-note{position:absolute;top:493px;font-family:"Domine",serif;font-size:15px;line-height:1.15;color:var(--ink-soft);
    text-align:left}
  .side-note.left{left:14px}
  .side-note.right{right:10px;text-align:right}
  .brand-mark{position:absolute;left:105px;width:120px;top:500px;display:flex;align-items:center;justify-content:center;gap:6px;
    font-family:"Domine",serif;font-weight:700;font-size:15px;color:var(--ink)}
  .brand-mark .dot{width:10px;height:10px;border-radius:50%;background:var(--ink);flex:none}
  .spec{position:absolute;top:638px;width:90px;font-family:"Domine",serif;font-size:14px;color:var(--ink-soft)}
  .spec .field{display:block;margin:12px auto 0;background:var(--field)}
  .spec.barrel{left:-2px}
  .spec.barrel .field{width:45px;height:38px}
  .spec.aged{left:120px}
  .spec.aged .field{width:80px;height:46px;margin-top:10px}
  .spec.alc{right:-2px}
  .spec.alc .field{width:45px;height:38px}
  .spec .unit{display:block;margin-top:8px}

  /* back */
  .back-brand{top:40px;display:flex;flex-direction:column;align-items:center;font-family:"Domine",serif;font-weight:700;color:var(--ink)}
  .back-brand .dot{width:36px;height:36px;border-radius:50%;background:var(--ink);margin-bottom:18px}
  .back-brand .name{font-size:19px;line-height:1.15}
  .company{top:156px;display:flex;align-items:center;justify-content:center;gap:8px;font-family:"Oswald",sans-serif;
    font-size:10px;letter-spacing:3px;color:var(--ink-soft)}
  .company::before,.company::after{content:"";width:22px;height:1px;background:var(--ink-soft)}
  .series-title{top:183px;font-family:"Pinyon Script",cursive;font-size:40px;line-height:1;font-weight:400}
  .edition{top:246px;font-family:"Domine",serif;font-weight:700;font-size:14px;line-height:1.35}
  .story{top:300px;left:42px;right:42px;font-family:"Oswald",sans-serif;font-weight:300;font-size:11.6px;line-height:19px;color:var(--ink-soft)}
  .producer{top:459px;font-family:"Domine",serif;font-weight:700;font-size:11px;line-height:1.3}
  .website{top:505px;font-family:"Domine",serif;font-size:20px;letter-spacing:.3px}
  .volume{top:554px;font-family:"Domine",serif;font-weight:700;font-size:15px}
  .warning{top:602px;left:12px;right:12px;font-family:"Oswald",sans-serif;font-weight:300;font-size:8.4px;line-height:13px;color:var(--ink-soft)}
</style>
</head>
<body>
<main class="canvas">

  <section class="label front-label" aria-label="Front label">
    <div class="horse-photo" role="img" aria-label="Black and white photograph of the stable's racehorse galloping with jockey"></div>
    <div class="est-tag left">EST</div>
    <div class="est-tag right">2016</div>
    <h1 class="abs brand-wordmark"><span>NIGHTFALL</span></h1>
    <div class="abs product-line"><p class="product-type">STRAIGHT BOURBON WHISKEY</p></div>
    <p class="side-note left">SINGLE<br>BARREL</p>
    <div class="brand-mark"><span class="dot"></span>NIGHTFALL</div>
    <p class="side-note right">BARREL<br>STRENGTH</p>
    <div class="spec barrel">BARREL N°<span class="field"></span></div>
    <div class="spec aged">AGED<span class="field"></span><span class="unit">YEARS</span></div>
    <div class="spec alc">ALC/VOL<span class="field"></span></div>
  </section>

  <section class="label back-label" aria-label="Back label">
    <div class="abs back-brand"><span class="dot"></span><span class="name">NIGHTFALL<br>BARREL</span></div>
    <p class="abs company">COMPANY</p>
    <h2 class="abs series-title">Winner Series</h2>
    <p class="abs edition">STORMING VALE EDITION<br>SINGLE BARREL N°45</p>
    <p class="abs story">The Nightfall Racing Winners Series honors the horses who have brought home victories for our stable. This edition celebrates Storming Vale and her maiden victory on May 28, 2021. Raise a glass to her incredible career with this non-chill filtered single barrel crafted in her honor. Here's to Storming Vale—a true champion!</p>
    <p class="abs producer">BOTTLED BY OLD MILLBROOK WHISKEY CO.<br>MILLBROOK, KENTUCKY<br>DISTILLED IN CEDAR FALLS, KENTUCKY</p>
    <p class="abs website">NIGHTFALL-SPIRITS.COM</p>
    <p class="abs volume">750 ML</p>
    <p class="abs warning">Government warning: (1) According to the surgeon general, women should not drink alcoholic beverages during pregnancy because of the risk of birth defects. (2) Consumption of alcoholic beverages impairs your ability to drive a car or operate machinery and may cause health problems.</p>
  </section>

</main>
</body>
</html>
```